Top Service Company Billboard for busiest highway in County

Top Service company seeks a NEW design for Billboard across highest traffic road in Country - more than 500,000 cars per day.

KRV is a residential services company, providing our clients with, Cleaning, maintenance, Pest Control and AC Duct Cleaning.

Please see ATTACHED specifications -

3 Must HAVES
Envision the company photo being the center/core of the message -
KRV Cleaning
Prices starting at AED 25

Target Market(s)

Residential Home Owners & Renters

Industry/Entity Type

Residential

Font styles to use
Serif

Colors

Designer to choose colors to be used in the design.

Requirements
Must have
• This Billboard must be in half Arabic and English - please see attached specifications
• As well please check attached for height & width requirements.
• This billboard must really pop -
• Envision the company photo being the center/core of the message -
• KRV Cleaning
• Prices starting at AED 25
• Need a catch phrase...
Nice to have
• + KRV Pest Control + Bravo Mend Up Logo if possible
Should not have
• Should not be English only

```html
<!DOCTYPE html>
<html lang="en">
<head>
<meta charset="utf-8">
<title>KRV Cleaning Billboard</title>
<link rel="stylesheet" href="https://fonts.googleapis.com/css2?family=Cairo:wght@600;700;800&family=Libre+Baskerville:wght@700&family=Open+Sans:wght@700;800&display=swap">
<style>
  :root {
    --stage: #3d3d3e;
    --panel: #f3f4f6;
    --blue: #1565b8;
    --blue-deep: #0d4a8c;
    --brown: #6b3f1e;
    --plum: #3a1a32;
    --violet: #5a2d6e;
    --ink: #1b1b1b;
    --photo-a: #8fa0a8;
    --photo-b: #d98aa8;
    --art-a: #ffffff;
    --art-b: #bdbdbd;
  }
  * { margin: 0; padding: 0; box-sizing: border-box; }
  html, body { width: 1200px; height: 171px; overflow: hidden; background: var(--stage); }
  .billboard {
    position: absolute; left: 42px; top: 42px; width: 1116px; height: 86px;
    background: var(--panel); overflow: hidden;
  }
  .brand { position: absolute; left: 0; top: 0; width: 158px; height: 86px; }
  .brand-mark {
    position: absolute; left: 22px; top: 16px; width: 22px; height: 22px;
    border-radius: 50%; background: var(--violet);
  }
  .brand-name {
    position: absolute; left: 52px; top: 10px;
    font-family: "Libre Baskerville", serif; font-weight: 700; font-size: 22px;
    color: var(--violet); line-height: 1;
  }
  .brand-sub {
    position: absolute; left: 52px; top: 34px;
    font-family: "Libre Baskerville", serif; font-weight: 700; font-size: 10px;
    color: var(--violet); letter-spacing: 0.5px;
  }
  .catchphrase {
    position: absolute; left: 18px; top: 62px;
    font-family: "Open Sans", sans-serif; font-weight: 700; font-size: 11.5px; color: var(--ink);
  }
  .price-en { position: absolute; left: 158px; top: 0; width: 92px; height: 86px; }
  .price-en svg, .price-ar svg, .ask svg, .divider { position: absolute; left: 0; top: 0; }
  .price-tab-text {
    position: absolute; top: 4px; text-align: center;
    font-family: "Open Sans", sans-serif; font-weight: 700; font-size: 11px; line-height: 1.2;
    color: #fff; white-space: nowrap;
  }
  .price-en .price-tab-text { left: 1px; width: 74px; }
  .price-value {
    position: absolute; text-align: center; white-space: nowrap;
    font-family: "Open Sans", sans-serif; font-weight: 700; font-size: 11.5px; line-height: 1.15;
    color: var(--ink);
  }
  .price-en .price-value { left: 8px; width: 70px; top: 54px; }
  .illustration {
    position: absolute; left: 252px; top: 3px; width: 90px; height: 80px;
    background: linear-gradient(135deg, var(--art-a), var(--art-b));
    border-radius: 4px;
  }
  .team-photo {
    position: absolute; left: 355px; top: 0; width: 405px; height: 86px;
    background: linear-gradient(180deg, #c9cdd0 0%, var(--photo-a) 35%, var(--photo-b) 75%, #7c7a80 100%);
  }
  .price-ar { position: absolute; left: 758px; top: 0; width: 94px; height: 86px; }
  .price-ar .price-tab-text {
    left: 17px; width: 72px; top: 10px; font-family: "Cairo", sans-serif; font-size: 11px;
  }
  .price-ar .price-value {
    left: 20px; width: 64px; top: 60px; font-family: "Cairo", sans-serif; font-size: 11.5px;
  }
  .ask { position: absolute; left: 850px; top: 0; width: 92px; height: 86px; }
  .ask-text {
    position: absolute; left: 12px; top: 14px; width: 72px; text-align: center;
    font-family: "Cairo", sans-serif; font-weight: 700; font-size: 15px; line-height: 1.3;
    color: #fff;
  }
  .brand-ar {
    position: absolute; left: 946px; top: 0; width: 164px; height: 86px; text-align: center;
    font-family: "Cairo", sans-serif; font-weight: 800; direction: rtl;
  }
  .brand-ar .line-top { position: absolute; right: 0; top: 8px; width: 164px; font-size: 21px; color: var(--violet); line-height: 1.2; }
  .brand-ar .line-bottom { position: absolute; right: 0; top: 34px; width: 164px; font-size: 30px; color: var(--plum); line-height: 1.2; }
</style>
</head>
<body>
<main class="billboard">
  <section class="brand">
    <span class="brand-mark"></span>
    <span class="brand-name">KRV</span>
    <span class="brand-sub">CLEANING</span>
    <p class="catchphrase">Need a catchphrase...</p>
  </section>

  <section class="price-en">
    <svg width="92" height="86" viewBox="0 0 92 86">
      <rect x="1" y="0" width="74" height="42" fill="var(--blue-deep)"/>
      <path d="M75 42 Q84 50 92 86 L88 86 Q80 52 71 44 Z" fill="var(--blue)"/>
    </svg>
    <p class="price-tab-text">Prices<br>starting</p>
    <p class="price-value">at 25<br>dharam</p>
  </section>

  <div class="illustration" role="img" aria-label="Cartoon cleaner with a hammer chasing a cockroach"></div>

  <div class="team-photo" role="img" aria-label="Company team photo: large staff group in pink and white uniforms with service vans behind"></div>
  <svg class="divider" style="left:355px" width="18" height="86" viewBox="0 0 18 86">
    <polygon points="0,0 6,0 18,86 12,86" fill="var(--blue)"/>
  </svg>
  <svg class="divider" style="left:746px" width="14" height="86" viewBox="0 0 14 86">
    <polygon points="8,0 14,0 6,86 0,86" fill="var(--blue)"/>
  </svg>

  <section class="price-ar">
    <svg width="94" height="86" viewBox="0 0 94 86">
      <rect x="2" y="0" width="92" height="86" fill="var(--panel)"/>
      <rect x="17" y="0" width="72" height="42" fill="var(--blue-deep)"/>
      <path d="M17 42 Q8 50 2 86 L6 86 Q12 52 21 44 Z" fill="var(--blue)"/>
    </svg>
    <p class="price-tab-text" dir="rtl">تبدأ الأسعار</p>
    <p class="price-value" dir="rtl">في 25 درهم</p>
  </section>

  <section class="ask">
    <svg width="92" height="86" viewBox="0 0 92 86">
      <polygon points="0,0 74,0 92,43 74,86 0,86 12,43" fill="var(--brown)"/>
    </svg>
    <p class="ask-text" dir="rtl">تحتاج إلى<br>شعار...</p>
  </section>

  <section class="brand-ar">
    <span class="line-top">كي آر في خدمات</span>
    <span class="line-bottom">التنظيف</span>
  </section>
</main>
</body>
</html>
```